Party Favors and Decorations Business Needs A Business Card Design

We are in need of a Logo design and business card design for a new small business called Lark Meadow Designs. We create party decorations and favours for Bridal Showers, Baby Showers, Weddings Birthdays etc. This is a very personalized service based on Clients theme, colour, and style. We are looking for a high end elegant look. I have attached a file to the style I like including the type of paper.

Target Market(s)

women, young adults, expectant mothers, mothers

Industry/Entity Type

Small Business

Contact Information for Business Card

Lark Meadow Designs Essex, ON 519-608-1942 larkmeadowdesigns.ca dana@larkmeadowgiftwrapping.com find us on Friendlink

Logo Text

Lark Meadow Designs

Font styles to use
Script

Requirements
Must have
• Name, email, web address, phone number
Should not have
• cutesy graphics

```html
<!DOCTYPE html>
<html lang="en">
<head>
<meta charset="utf-8">
<title>Lark Meadow Designs – Business Card</title>
<link rel="stylesheet" href="https://fonts.googleapis.com/css2?family=Cormorant+Garamond:wght@500&family=Open+Sans:wght@400;600&display=swap">
<style>
  :root {
    --ink: #0d0d0d;
    --paper: #f4f4f4;
    --paper-shade: #dcdcdc;
    --rule-dark: #111111;
    --grey-text: #3a3a3a;
    --stage: #e6e4e0;
  }
  * { margin: 0; padding: 0; box-sizing: border-box; }
  html, body { width: 1200px; height: 885px; overflow: hidden; }
  body {
    background: var(--stage);
    font-family: "Open Sans", sans-serif;
    display: flex;
    flex-direction: column;
    align-items: center;
    justify-content: center;
    gap: 56px;
  }
  .card {
    position: relative;
    width: 630px;
    height: 360px;
    background: linear-gradient(180deg, #ffffff 0%, var(--paper) 60%, var(--paper-shade) 100%);
    box-shadow: 0 6px 18px rgba(0,0,0,0.25);
    overflow: hidden;
  }
  .rule {
    position: absolute; left: 0; right: 0; height: 2px;
    background: var(--rule-dark);
  }

  .wordmark {
    font-family: "Cormorant Garamond", serif;
    font-weight: 500;
    line-height: 1;
  }
  .wordmark span { display: block; }

  /* ---------- front ---------- */
  .front .band {
    position: absolute;
    left: 0; right: 0;
    top: 200px; height: 118px;
    background: linear-gradient(180deg, #1c1c1c, var(--ink) 40%, #000);
  }
  .front .rule.above { top: 190px; }
  .front .rule.below { top: 328px; }

  .front .wordmark {
    position: absolute;
    left: 40px; top: 62px;
    width: 300px;
    font-size: 42px;
    color: var(--ink);
  }
  .front .person {
    position: absolute;
    right: 42px; top: 52px;
    text-align: right;
  }
  .person .name {
    font-weight: 600; font-size: 22px; color: var(--grey-text);
  }
  .person .role {
    font-size: 14px; color: #555; margin-top: 2px;
  }

  .contacts {
    position: absolute;
    left: 40px; top: 222px;
    list-style: none;
    color: #f2f2f2;
    font-size: 15px;
  }
  .contacts li {
    display: flex; align-items: center; gap: 10px;
    height: 25px;
  }
  .contacts svg { width: 16px; height: 16px; flex: none; }

  .social {
    position: absolute;
    right: 42px; top: 240px;
    display: flex; align-items: center; gap: 8px;
    color: #ffffff;
  }
  .social .mark-square {
    width: 30px; height: 30px; background: #ffffff;
  }
  .social .lead { font-size: 11px; display: block; }
  .social .network { font-size: 18px; font-weight: 600; display: block; line-height: 1.1; }

  /* ---------- back ---------- */
  .back .band {
    position: absolute;
    left: 0; right: 0;
    top: 62px; height: 190px;
    background: linear-gradient(180deg, #1e1e1e, var(--ink) 45%, #000);
  }
  .back .rule.above { top: 52px; }
  .back .rule.below { top: 262px; }
  .back .wordmark {
    position: absolute;
    left: 0; right: 0; top: 104px;
    text-align: center;
    font-size: 52px;
    color: #ffffff;
  }
</style>
</head>
<body>

  <section class="card front" aria-label="Business card front">
    <div class="wordmark"><span>Lark Meadow</span><span>Designs</span></div>
    <div class="person">
      <div class="name">Employee Name</div>
      <div class="role">Managing Director</div>
    </div>

    <div class="rule above"></div>
    <div class="band"></div>
    <div class="rule below"></div>

    <ul class="contacts">
      <li>
        <svg viewBox="0 0 16 16" aria-hidden="true"><rect width="16" height="16" rx="2" fill="#e8e8e8"/><path d="M4.5 3.5l2 0 1 2.5-1.3 1a6 6 0 0 0 2.8 2.8l1-1.3 2.5 1v2a1 1 0 0 1-1 1A8 8 0 0 1 3.5 4.5a1 1 0 0 1 1-1z" fill="#111"/></svg>
        519-608-1942
      </li>
      <li>
        <svg viewBox="0 0 16 16" aria-hidden="true"><rect width="16" height="16" rx="2" fill="#e8e8e8"/><circle cx="8" cy="8" r="5" fill="none" stroke="#111" stroke-width="1.2"/><ellipse cx="8" cy="8" rx="2.2" ry="5" fill="none" stroke="#111" stroke-width="1"/><line x1="3" y1="8" x2="13" y2="8" stroke="#111" stroke-width="1"/></svg>
        larkmeadowdesigns.ca
      </li>
      <li>
        <svg viewBox="0 0 16 16" aria-hidden="true"><rect width="16" height="16" rx="2" fill="#e8e8e8"/><rect x="3" y="4.5" width="10" height="7" fill="none" stroke="#111" stroke-width="1.2"/><path d="M3 4.5l5 4 5-4" fill="none" stroke="#111" stroke-width="1.2"/></svg>
        dana@larkmeadowgiftwrapping.com
      </li>
    </ul>

    <div class="social">
      <span class="mark-square" aria-hidden="true"></span>
      <span>
        <span class="lead">Find us on</span>
        <span class="network">Friendlink</span>
      </span>
    </div>
  </section>

  <section class="card back" aria-label="Business card back">
    <div class="rule above"></div>
    <div class="band"></div>
    <div class="rule below"></div>
    <div class="wordmark"><span>Lark Meadow</span><span>Designs</span></div>
  </section>

</body>
</html>
```